VLM8 Business Card Design Project

Design which catches the client with the first impression. A design which is professional and classy with elegance. We have also got another project running and the winning prize for that is $240 "vlm8 print + graphic design".
For all the company details please visit www.vlm8-example.com.
Please find the logo attached and i would like to have good colors for my business card.
, Design which catches the client with the first impression. A design which is professional and classy with elegance.
Updates
VLM8 is running two projects at the same time, please feel free to participate. The other project name is

```html
<!DOCTYPE html>
<html lang="en">
<head>
<meta charset="utf-8">
<title>VLM8 Business Card</title>
<link rel="stylesheet" href="https://fonts.googleapis.com/css2?family=Open+Sans:wght@400;600&display=swap">
<style>
  :root {
    --backdrop: #d8d4cf;
    --card-dark: #262b2c;
    --card-dark-edge: #2d3334;
    --lime: #9dcb3b;
    --teal: #2fa77f;
    --brand-green: #2db58a;
    --bullet: #8cc63f;
    --ink-dark: #1f2424;
    --ink-light: #e9eeec;
  }
  * { margin: 0; padding: 0; box-sizing: border-box; }
  html, body {
    width: 1200px;
    height: 748px;
    overflow: hidden;
    background: var(--backdrop);
    font-family: "Open Sans", Arial, sans-serif;
  }
  .card {
    position: absolute;
    left: 170px;
    top: 128px;
    width: 860px;
    height: 492px;
    background: var(--card-dark);
    box-shadow: 0 10px 30px rgba(0, 0, 0, 0.25);
    overflow: hidden;
  }
  .lime-band {
    position: absolute;
    left: 54px;
    top: 0;
    width: 246px;
    height: 100%;
    background: var(--lime);
  }
  .edge-tab {
    position: absolute;
    top: 144px;
    width: 25px;
    height: 204px;
    background: var(--teal);
  }
  .edge-tab--left { left: 0; }
  .edge-tab--right { left: 832px; }

  .company-name {
    position: absolute;
    left: 87px;
    top: 176px;
    font-size: 30px;
    font-weight: 400;
    color: var(--ink-dark);
    white-space: nowrap;
  }
  .address {
    position: absolute;
    left: 87px;
    top: 226px;
    font-size: 16px;
    line-height: 19.5px;
    color: var(--ink-dark);
    font-style: normal;
  }
  .contact {
    position: absolute;
    left: 87px;
    top: 338px;
    font-size: 16px;
    line-height: 21px;
    color: var(--ink-dark);
  }
  .contact b { font-weight: 600; margin-right: 8px; }

  .brand {
    position: absolute;
    left: 415px;
    top: 160px;
    display: flex;
    align-items: center;
    gap: 14px;
  }
  .brand-dot {
    width: 44px;
    height: 44px;
    border-radius: 50%;
    background: var(--lime);
  }
  .brand-name {
    font-size: 54px;
    font-weight: 600;
    line-height: 1;
    color: var(--brand-green);
    letter-spacing: 1px;
  }

  .services {
    position: absolute;
    left: 430px;
    top: 233px;
    list-style: none;
  }
  .services li {
    position: relative;
    padding-left: 24px;
    font-size: 20px;
    line-height: 33px;
    color: var(--ink-light);
    white-space: nowrap;
  }
  .services li::before {
    content: "";
    position: absolute;
    left: 0;
    top: 12px;
    width: 10px;
    height: 10px;
    border-radius: 50%;
    background: var(--bullet);
  }
</style>
</head>
<body>
  <section class="card" aria-label="VLM8 business card">
    <div class="lime-band"></div>
    <div class="edge-tab edge-tab--left"></div>
    <div class="edge-tab edge-tab--right"></div>

    <h1 class="company-name">VLM8 Pty Ltd</h1>
    <address class="address">
      118 Harbourline Road<br>
      7th Street Elmwood<br>
      Riverton<br>
      Kestal<br>
      390415
    </address>
    <p class="contact">
      <span><b>T:</b>380.555.0192</span><br>
      <span><b>W:</b>www.vlm8-example.com</span>
    </p>

    <div class="brand">
      <span class="brand-dot"></span>
      <span class="brand-name">VLM8</span>
    </div>
    <ul class="services">
      <li>Information Technology</li>
      <li>Food Services</li>
      <li>Lighting</li>
      <li>Child Care Centres</li>
      <li>Extreme Sports</li>
    </ul>
  </section>
</body>
</html>
```